NZ First of it's kind solutions directory and marketplace for busy Mums needs a business card design

We need a business card design for our new nationwide business in NZ (long term plans to go global). We provide solutions to the everyday challenges that busy Mums face by connecting them with quality communities and suppliers of carefully selected, relevant products and services. We sell direct via our online marketplace. The final design should communicate our values of inclusivity, quality and smart solutions. Colours should incorporate our logo colour palette of #477077 and #6ba8b2. Our website is at https://www.brightnestly.com

Target Market(s)

busy Mums, Age 28 – 50, female, income over $100K, location main centres NZ primarily but NZ wide. Is likely juggling work or career with a young family. Probably had hobbies which have fallen by the wayside.
-Wants to succeed in her chosen career without compromising on family life
-to successfully juggle her career without feeling like she is compromising her children
- Is time poor, something always has to give and it’s generally her health (she’ll stay up late, get stressed)
- probably ex corporate or professional career. Has discretional income

Industry/Entity Type

Business

Contact Information for Business Card

Jodie Farnsworth, Founder, BrightNestly.com (Strapline Browse; Pick; Sorted), 48 Kowhai Terrace, Hillsborough, Auckland 1058, New Zealand. Mob: 021 437 518 Ph: +64 (0)9 584 7163

Font styles to use
Other font styles liked:
• Raleway, and/or Architects Daughter

Colors
00a990
33b8a4
86cfc6
cfeae6

Requirements
Must have
• the above details, streamline. the logo and colours associated with those logos
Should not have
• foil or metallic colours

```html
<!DOCTYPE html>
<html lang="en">
<head>
<meta charset="utf-8">
<title>BrightNestly — Business Card</title>
<link rel="stylesheet" href="https://fonts.googleapis.com/css2?family=Raleway:wght@400;500;700;800&display=swap">
<style>
  :root {
    --teal: #00a990;
    --teal-mid: #33b8a4;
    --mint: #86cfc6;
    --mint-pale: #cfeae6;
    --slate: #477077;
    --slate-light: #6ba8b2;
    --paper: #ffffff;
    --backdrop: #e4e5e4;
  }
  * { box-sizing: border-box; margin: 0; padding: 0; }
  html, body {
    width: 1200px;
    height: 1000px;
    overflow: hidden;
  }
  body {
    position: relative;
    background: var(--backdrop);
    font-family: "Raleway", sans-serif;
  }

  /* Front of card */
  .card-front {
    position: absolute;
    left: 170px;
    top: 112px;
    width: 590px;
    height: 338px;
    background: var(--teal);
  }
  .card-front .frame {
    position: absolute;
    left: 28px;
    top: 29px;
    width: 536px;
    height: 280px;
    border: 2px solid var(--paper);
  }
  .card-front .brand {
    position: absolute;
    left: 0;
    right: 0;
    top: 128px;
    display: flex;
    justify-content: center;
    align-items: center;
    gap: 16px;
  }
  .card-front .brand-dot {
    width: 40px;
    height: 40px;
    border-radius: 50%;
    background: var(--mint-pale);
  }
  .card-front .brand-name {
    font-size: 44px;
    font-weight: 800;
    color: var(--paper);
    letter-spacing: -0.5px;
  }

  /* Back of card */
  .card-back {
    position: absolute;
    left: 389px;
    top: 557px;
    width: 598px;
    height: 341px;
    background: var(--paper);
  }
  .card-back .brand {
    position: absolute;
    left: 30px;
    top: 38px;
    display: flex;
    align-items: center;
    gap: 10px;
  }
  .card-back .brand-dot {
    width: 26px;
    height: 26px;
    border-radius: 50%;
    background: var(--slate);
  }
  .card-back .brand-name {
    font-size: 27px;
    font-weight: 800;
    color: var(--slate);
    letter-spacing: -0.3px;
  }
  .person {
    position: absolute;
    left: 0;
    width: 598px;
    top: 98px;
    padding-left: 0;
    text-align: center;
    transform: translateX(0);
  }
  .person .name {
    display: block;
    width: 300px;
    margin-left: 149px;
    font-size: 28px;
    font-weight: 500;
    color: var(--teal);
    line-height: 1.1;
  }
  .person .role {
    display: block;
    width: 300px;
    margin-left: 149px;
    margin-top: 4px;
    font-size: 18px;
    font-weight: 400;
    color: var(--teal);
  }
  .rule {
    position: absolute;
    left: 0;
    top: 163px;
    width: 598px;
    height: 2px;
    background: var(--teal);
  }
  .address-band {
    position: absolute;
    left: 58px;
    top: 164px;
    width: 484px;
    height: 26px;
  }
  .address-band svg { position: absolute; inset: 0; }
  .address-band .address {
    position: relative;
    display: block;
    text-align: center;
    line-height: 26px;
    font-size: 14.5px;
    font-weight: 500;
    color: var(--paper);
  }
  .contact-list {
    position: absolute;
    left: 44px;
    top: 208px;
    list-style: none;
  }
  .contact-list li {
    display: flex;
    align-items: center;
    height: 32.5px;
    font-size: 18px;
    color: var(--teal);
  }
  .contact-list .icon {
    width: 22px;
    height: 22px;
    margin-right: 15px;
    flex: none;
  }
  .contact-list .strapline {
    font-size: 13px;
    margin-left: 6px;
  }
</style>
</head>
<body>

  <section class="card-front" aria-label="Card front">
    <div class="frame"></div>
    <div class="brand">
      <span class="brand-dot"></span>
      <span class="brand-name">BrightNestly</span>
    </div>
  </section>

  <section class="card-back" aria-label="Card back">
    <div class="brand">
      <span class="brand-dot"></span>
      <span class="brand-name">BrightNestly</span>
    </div>

    <div class="person">
      <span class="name">Jodie Farnsworth</span>
      <span class="role">Founder</span>
    </div>

    <div class="rule"></div>

    <div class="address-band">
      <svg viewBox="0 0 484 26" width="484" height="26" aria-hidden="true">
        <path d="M0 0 H484 Q478 26 462 26 H22 Q6 26 0 0 Z" fill="var(--teal)"/>
      </svg>
      <span class="address">48 Kowhai Terrace, Hillsborough, Auckland 1058, New Zealand</span>
    </div>

    <ul class="contact-list">
      <li>
        <svg class="icon" viewBox="0 0 24 24" aria-hidden="true">
          <path d="M3 9 Q12 3 21 9 L19 11.5 L16 10.5 L15.5 8.5 Q12 7.5 8.5 8.5 L8 10.5 L5 11.5 Z" fill="var(--teal)"/>
          <path d="M7 12 H17 L19 20 H5 Z" fill="var(--teal)"/>
          <circle cx="12" cy="16" r="2.2" fill="var(--paper)"/>
        </svg>
        <span>+64 (0)9 584 7163</span>
      </li>
      <li>
        <svg class="icon" viewBox="0 0 24 24" aria-hidden="true">
          <path d="M6.5 3 L9.5 3 L11 7.5 L8.8 9.2 Q10.5 13 14.8 15.2 L16.5 13 L21 14.5 L21 17.5 Q20 21 16.5 20.5 Q6 18 3.5 7.5 Q3 4 6.5 3 Z" fill="var(--teal)"/>
        </svg>
        <span>021 437 518</span>
      </li>
      <li>
        <svg class="icon" viewBox="0 0 24 24" aria-hidden="true" fill="none" stroke="var(--teal)" stroke-width="2">
          <circle cx="12" cy="12" r="9"/>
          <ellipse cx="12" cy="12" rx="4" ry="9"/>
          <path d="M3 12 H21 M4.5 7.5 H19.5 M4.5 16.5 H19.5"/>
        </svg>
        <span>www.brightnestly.com</span>
        <span class="strapline">( Strapline Browse; Pick; Sorted )</span>
      </li>
    </ul>
  </section>

</body>
</html>
```